Power point Presentation Template 2

I am looking a professionally designed Powerpoint Presentation template for my company. We are Information Technology Company. I have attached the Logo. The Logo will also give an indication of which colours to be used in the design.

Target Market(s)

Information and Communication Technology

Requirements
Must have
• All ideas welcomed
Nice to have
• Professional Look and Feel

```html
<!DOCTYPE html>
<html lang="en">
<head>
<meta charset="utf-8">
<title>Nexora Technologies – Presentation Template</title>
<link rel="stylesheet" href="https://fonts.googleapis.com/css2?family=Open+Sans:wght@400;600;700;800&display=swap">
<style>
:root{
  --orange:#f7941d;
  --orange-deep:#e4731a;
  --brown:#7b3a1c;
  --charcoal:#464646;
  --ink:#3a3a3a;
  --muted:#8a8a8a;
  --sorter-bg:#e9e9e9;
  --slide-bg:#ffffff;
  --slide-edge:#d2d2d2;
  --accent-red:#c8352a;
  --photo-grey:#c9c6c1;
  --photo-warm:#d8b48a;
  --photo-dark:#4c4f55;
  --photo-blue:#3a4a60;
}
*{box-sizing:border-box;margin:0;padding:0}
html,body{width:1200px;height:581px;overflow:hidden}
body{background:var(--sorter-bg);font-family:"Open Sans",Arial,sans-serif;color:var(--ink);position:relative}
.top-rule{position:absolute;left:0;top:0;width:1200px;height:2px;background:var(--accent-red)}
.drop-marker{position:absolute;left:1006px;top:496px;width:1px;height:82px;background:var(--accent-red)}
.drop-marker::before{content:"";position:absolute;left:-3px;top:0;width:7px;height:1px;background:var(--accent-red)}

.thumb{position:absolute;width:125px;height:92px}
.slide{position:relative;width:125px;height:72px;background:var(--slide-bg);border:1px solid var(--slide-edge);overflow:hidden}
.num{position:absolute;left:1px;top:77px;font-size:11px;color:#555}
.star{position:absolute;right:2px;top:78px;font-size:9px;color:#666}

.t{position:absolute;font-size:4.4px;font-weight:700;color:var(--orange);left:5px;top:4px;white-space:nowrap}
.logo{position:absolute;right:4px;top:3px;font-size:3.6px;font-weight:700;color:var(--orange);display:flex;align-items:center;gap:1.5px;letter-spacing:.2px}
.logo i{display:block;width:3px;height:3px;background:var(--orange)}
.logo.white{color:#fff}.logo.white i{background:#fff}
.p{position:absolute;font-size:2.1px;line-height:2.9px;color:var(--ink)}
.p li{list-style:none;margin-bottom:1px;padding-left:2px;position:relative}
.p li::before{content:"";position:absolute;left:0;top:1px;width:.8px;height:.8px;background:var(--orange)}
.foot{position:absolute;left:0;right:0;bottom:3px;height:.6px;background:var(--orange)}
.photo{position:absolute}

.band{position:absolute;left:0;right:0;display:flex;align-items:center;justify-content:space-between;padding:0 6px}
.band b{color:#fff;font-weight:800;font-size:6.5px;line-height:7.5px}
.box{position:absolute;font-size:2px;line-height:2.7px;color:#fff;padding:1.5px;text-align:center}
</style>
</head>
<body>
<div class="top-rule"></div>

<!-- Row 1 -->
<div class="thumb" style="left:20px;top:9px">
  <div class="slide">
    <div class="photo" role="img" aria-label="Office desk photograph" style="left:0;top:0;right:0;height:32px;background:linear-gradient(90deg,#e9e6e1,#cfcac2)"></div>
    <div class="band" style="top:32px;height:22px;background:var(--orange)"><b style="font-size:7.5px">Company Profile</b><span class="logo white" style="position:static;font-size:4px"><i></i>NEXORA</span></div>
    <div class="p" style="left:6px;top:58px;color:var(--muted);font-size:2.6px">Profile edition 2019 | IT services</div>
  </div><span class="num">1</span>
</div>

<div class="thumb" style="left:187px;top:9px">
  <div class="slide">
    <div class="t">Company Profile</div>
    <div class="p" style="left:6px;top:18px;width:38px"><b style="color:var(--orange)">Head Office</b><br>T: 000 000 0000<br>F: 000 000 0001<br>E: hello@nexora.example</div>
    <div class="logo" style="right:14px;top:28px;font-size:8px;gap:3px;flex-direction:row"><i style="width:9px;height:9px"></i>NEXORA</div>
    <div class="p" style="right:14px;top:38px;font-size:3px;color:var(--muted);letter-spacing:.6px">TECHNOLOGIES</div>
    <div class="foot"></div>
  </div><span class="num">2</span>
</div>

<div class="thumb" style="left:354px;top:9px">
  <div class="slide">
    <div class="logo" style="left:40px;right:auto;top:12px;font-size:8px;gap:3px"><i style="width:9px;height:9px"></i>NEXORA</div>
    <div class="t" style="top:31px;font-size:4px">BACKGROUND</div>
    <div class="p" style="left:5px;top:38px;width:115px">Nexora Technologies was founded in 2010 as a private company and grew into a trusted provider of managed IT, networks and hosting for clients across many industries in the region.</div>
  </div><span class="num">3</span>
</div>

<div class="thumb" style="left:521px;top:9px">
  <div class="slide">
    <div class="t">BACKGROUND</div>
    <div class="photo" role="img" aria-label="Person writing at a desk" style="right:0;top:0;width:60px;height:72px;background:linear-gradient(135deg,#d9cdbd,#9c8a74)"></div>
    <div class="p" style="left:5px;top:14px;width:56px">Our company is built on the conviction that good technology management drives growth. We give clients one partner for support, networks, hosting and communication, with skilled engineers and clear service levels that keep every system running well and safe.</div>
  </div><span class="num">4</span>
</div>

<div class="thumb" style="left:688px;top:9px">
  <div class="slide">
    <div class="t" style="color:var(--ink)">Our key success factors include the following:</div>
    <div class="logo"><i></i>NEXORA</div>
    <div class="box" style="left:5px;top:14px;width:36px;height:20px;background:var(--orange)">Skilled people and steady delivery</div>
    <div class="box" style="left:44px;top:14px;width:36px;height:20px;background:var(--orange)">Trusted partners and tools</div>
    <div class="box" style="left:83px;top:14px;width:37px;height:20px;background:var(--charcoal)">Proactive support model</div>
    <div class="box" style="left:5px;top:40px;width:36px;height:22px;background:var(--orange)">Client focused service levels</div>
    <div class="box" style="left:44px;top:40px;width:76px;height:22px;background:var(--charcoal)">Flexible pricing and sound governance across all projects</div>
  </div><span class="num">5</span><span class="star">★</span>
</div>

<div class="thumb" style="left:855px;top:9px">
  <div class="slide">
    <div class="t" style="font-size:5px">MISSION STATEMENT</div>
    <div class="photo" role="img" aria-label="Hand touching a glowing network screen" style="right:0;top:0;width:50px;height:72px;background:linear-gradient(135deg,#2f4a6b,#8aa0bb)"></div>
    <ul class="p" style="left:5px;top:16px;width:66px"><li>To provide sound ICT and engineering solutions that create value for clients.</li><li>To grow with our clients and build lasting relationships.</li><li>To develop our people and uphold quality, integrity and service.</li></ul>
  </div><span class="num">6</span>
</div>

<div class="thumb" style="left:1022px;top:9px">
  <div class="slide">
    <div class="photo" role="img" aria-label="Office plant and desk photograph" style="left:0;top:0;width:65px;height:72px;background:linear-gradient(135deg,#ecebe6,#c5c2b8)"></div>
    <div style="position:absolute;right:0;top:0;width:60px;height:72px;background:var(--orange)"></div>
    <div class="t" style="color:#fff;left:72px;top:14px;font-size:4.6px">VISION STATEMENT</div>
    <div class="p" style="left:70px;top:26px;width:50px;color:#fff;text-align:center">To be a leading provider of innovative ICT solutions that help businesses grow.</div>
  </div><span class="num">7</span>
</div>

<!-- Row 2 -->
<div class="thumb" style="left:20px;top:132px">
  <div class="slide">
    <div class="t">Our Values</div><div class="logo"><i></i>NEXORA</div>
    <ul class="p" style="left:5px;top:14px;width:112px"><li>Nexora is committed to fair and ethical treatment of employees and all stakeholders at all times.</li><li>Nexora is a responsible corporate citizen that meets its duties to society.</li><li>Nexora strives to provide products and services of uncompromising quality.</li><li>Nexora treats partners with respect and communicates openly and honestly.</li><li>Nexora values every client relationship.</li></ul>
  </div><span class="num">8</span>
</div>

<div class="thumb" style="left:187px;top:132px">
  <div class="slide">
    <div class="photo" role="img" aria-label="Business people shaking hands" style="inset:0;background:linear-gradient(120deg,#c96f1f,#6e3b1a 60%,#3b2a22)"></div>
    <div class="band" style="top:24px;height:24px;background:rgba(70,70,70,.55)"><b>GOVERNANCE,<br>RISK AND ETHICS</b><span class="logo white" style="position:static;font-size:4px"><i></i>NEXORA</span></div>
  </div><span class="num">9</span>
</div>

<div class="thumb" style="left:354px;top:132px">
  <div class="slide">
    <div class="t">GOVERNANCE, RISK AND ETHICS</div><div class="logo"><i></i>NEXORA</div>
    <ul class="p" style="left:5px;top:14px;width:68px"><li>Nexora maintains a sound and transparent governance structure.</li><li>Our employees work to the highest standards of ethics and risk control.</li><li>Board oversight ensures accountability in every decision we take.</li></ul>
    <div class="photo" role="img" aria-label="Team joining hands" style="right:4px;top:16px;width:44px;height:30px;background:linear-gradient(135deg,#8a7a68,#3a3430)"></div>
  </div><span class="num">10</span>
</div>

<div class="thumb" style="left:521px;top:132px">
  <div class="slide">
    <div class="t">GOVERNANCE, RISK AND ETHICS</div><div class="logo"><i></i>NEXORA</div>
    <ul class="p" style="left:5px;top:13px;width:112px"><li>Nexora follows a clear code of conduct in all dealings.</li><li>Risks are reviewed regularly and managed by senior staff.</li></ul>
    <div class="box" style="left:5px;top:30px;width:37px;height:36px;background:var(--orange)"><b>INTEGRITY</b><br>We act honestly and keep our promises.</div>
    <div class="box" style="left:44px;top:30px;width:37px;height:36px;background:var(--charcoal)"><b>ACCOUNTABILITY</b><br>We own our work and results.</div>
    <div class="box" style="left:83px;top:30px;width:37px;height:36px;background:var(--charcoal)"><b>TRANSPARENCY</b><br>We share clear facts with clients.</div>
  </div><span class="num">11</span><span class="star">★</span>
</div>

<div class="thumb" style="left:688px;top:132px">
  <div class="slide">
    <div class="photo" role="img" aria-label="Collage of technology photographs" style="left:42px;top:4px;width:24px;height:18px;background:#6b6f76"></div>
    <div class="photo" role="img" aria-label="Server room photograph" style="left:68px;top:4px;width:24px;height:18px;background:#9aa3ad"></div>
    <div class="photo" role="img" aria-label="Cable photograph" style="left:94px;top:4px;width:26px;height:18px;background:#b98a55"></div>
    <div style="position:absolute;left:0;top:26px;width:70px;height:18px;background:var(--orange)"></div>
    <div class="t" style="color:#fff;top:28px;font-size:4.4px;line-height:5.4px;white-space:normal;width:62px">OUR SOLUTIONS AND SERVICE OFFERINGS</div>
    <div class="photo" role="img" aria-label="Office laptop photograph" style="left:74px;top:26px;width:46px;height:18px;background:#c9c3b8"></div>
    <div class="photo" role="img" aria-label="Desk with devices photograph" style="left:74px;top:48px;width:46px;height:20px;background:#5b5d62"></div>
  </div><span class="num">12</span>
</div>

<div class="thumb" style="left:855px;top:132px">
  <div class="slide">
    <div class="t">Infrastructure Solutions</div><div class="logo"><i></i>NEXORA</div>
    <ul class="p" style="left:5px;top:14px;width:112px"><li>We design, supply and install complete network and server infrastructure.</li><li>Cabling, switching, wireless and storage built to client needs.</li><li>Virtualisation and cloud migration planned with care.</li><li>Security appliances, firewalls and backup systems.</li><li>Power protection and data centre fit out.</li><li>Audits and health checks of current systems.</li></ul>
  </div><span class="num">13</span>
</div>

<div class="thumb" style="left:1022px;top:132px">
  <div class="slide">
    <div class="t">Managed Services</div><div class="logo"><i></i>NEXORA</div>
    <div class="photo" role="img" aria-label="Glowing network light photograph" style="left:5px;top:12px;width:115px;height:26px;background:linear-gradient(90deg,#1d2633,#6f87a6,#1d2633)"></div>
    <div class="p" style="left:5px;top:42px;width:115px"><b style="color:var(--orange)">Overview</b><br>Our managed services give clients round the clock monitoring, support and maintenance of their IT estate, so internal teams can focus on core business.</div>
  </div><span class="num">14</span>
</div>

<!-- Row 3 -->
<div class="thumb" style="left:20px;top:255px">
  <div class="slide">
    <div class="t" style="white-space:normal;width:60px;line-height:5px">Network, Server and Desktop Management</div>
    <div class="photo" role="img" aria-label="Network cables in a patch panel" style="right:0;top:0;width:52px;height:72px;background:linear-gradient(135deg,#d9d6cf,#7d8d5f 50%,#b7b2a8)"></div>
    <div class="p" style="left:5px;top:18px;width:64px">We monitor and manage networks, servers and desktops with proven tools. Our engineers keep systems patched, backed up and secure, and report clearly on uptime and health each month.</div>
  </div><span class="num">15</span>
</div>

<div class="thumb" style="left:187px;top:255px">
  <div class="slide">
    <div class="t">Helpdesk</div>
    <div class="photo" role="img" aria-label="Red telephone handset" style="right:0;top:0;width:50px;height:72px;background:linear-gradient(135deg,#f2eeee,#d8483c 60%,#efe9e9)"></div>
    <ul class="p" style="left:5px;top:15px;width:66px"><li>Our helpdesk gives users one point of contact.</li><li>Calls are logged, tracked and escalated by priority.</li><li>Remote and onsite help is ready when needed.</li><li>Reports show trends and fix rates.</li></ul>
  </div><span class="num">16</span>
</div>

<div class="thumb" style="left:354px;top:255px">
  <div class="slide">
    <div class="t" style="font-size:3.2px;color:var(--ink)">Our managed service includes</div>
    <svg style="position:absolute;left:42px;top:14px" width="42" height="42" viewBox="0 0 42 42" aria-hidden="true">
      <g fill="none" stroke-width="6">
        <circle cx="21" cy="21" r="15" stroke="var(--orange)" stroke-dasharray="11 1.6"/>
        <circle cx="21" cy="21" r="15" stroke="var(--charcoal)" stroke-dasharray="11 1.6" stroke-dashoffset="12.6" transform="rotate(45 21 21)" opacity=".9"/>
      </g>
    </svg>
    <div class="p" style="left:8px;top:16px;width:32px;border:.4px solid #bbb;padding:.5px">Service desk</div>
    <div class="p" style="left:4px;top:32px;width:34px;border:.4px solid #bbb;padding:.5px">Change management</div>
    <div class="p" style="left:8px;top:50px;width:32px;border:.4px solid #bbb;padding:.5px">Patch management</div>
    <div class="p" style="left:88px;top:16px;width:32px;border:.4px solid #bbb;padding:.5px">Security</div>
    <div class="p" style="left:90px;top:32px;width:30px;border:.4px solid #bbb;padding:.5px">Email</div>
    <div class="p" style="left:88px;top:50px;width:32px;border:.4px solid #bbb;padding:.5px">Backups</div>
  </div><span class="num">17</span><span class="star">★</span>
</div>

<div class="thumb" style="left:521px;top:255px">
  <div class="slide">
    <div class="t">Hosting Services</div>
    <div class="photo" role="img" aria-label="Server rack cables" style="right:0;top:0;width:52px;height:72px;background:linear-gradient(135deg,#dcdcd8,#7f8a6a 50%,#c0bcb4)"></div>
    <div class="p" style="left:5px;top:15px;width:64px">We are well placed to host critical systems in secure data centres. Clients gain uptime, fast links and expert care without buying their own hardware, and can scale as they grow with a clear monthly cost.</div>
  </div><span class="num">18</span>
</div>

<div class="thumb" style="left:688px;top:255px">
  <div class="slide">
    <div class="t">Hosting Services</div><div class="logo"><i></i>NEXORA</div>
    <div class="photo" role="img" aria-label="Fibre cables photograph" style="left:5px;top:13px;width:48px;height:52px;background:linear-gradient(135deg,#5b87b5,#d9a24a)"></div>
    <div class="p" style="left:58px;top:14px;width:60px">Our complete hosting services include:</div>
    <div class="p" style="left:58px;top:20px;width:60px;line-height:7.5px">
      <div>✔ Server hosting</div><div>✔ Virtualisation</div><div>✔ Email hosting</div><div>✔ Storage solutions</div><div>✔ Professional services</div>
    </div>
  </div><span class="num">19</span>
</div>

<div class="thumb" style="left:855px;top:255px">
  <div class="slide">
    <div class="t">Converged Communication</div><div class="logo"><i></i>NEXORA</div>
    <div class="p" style="left:5px;top:14px;width:66px">We bring voice, data and video onto one network. Unified communication lowers cost, simplifies support and links offices and mobile staff. Our team plans, installs and supports each system end to end.</div>
    <div class="p" style="left:80px;top:13px;width:40px;font-weight:700">Our offering includes:</div>
    <div class="box" style="left:77px;top:19px;width:20px;height:10px;background:var(--charcoal)">IP telephony</div>
    <div class="box" style="left:100px;top:19px;width:20px;height:10px;background:var(--charcoal)">Video conferencing</div>
    <div class="box" style="left:77px;top:32px;width:20px;height:10px;background:var(--charcoal)">Contact centre</div>
    <div class="box" style="left:100px;top:32px;width:20px;height:10px;background:var(--charcoal)">Mobility</div>
    <div class="box" style="left:88px;top:50px;width:20px;height:10px;background:#9a9a9a">Call billing</div>
  </div><span class="num">20</span><span class="star">★</span>
</div>

<div class="thumb" style="left:1022px;top:255px">
  <div class="slide">
    <div class="t">Managed Print Services</div>
    <div class="p" style="left:5px;top:12px;width:115px">Our managed print service reduces printing cost, controls usage and keeps devices working through monitoring and timely supply.</div>
    <div class="p" style="left:5px;top:24px;width:115px">We supply, install, repair and maintain:</div>
    <svg style="position:absolute;left:5px;top:34px" width="115" height="22" viewBox="0 0 115 22" aria-hidden="true">
      <line x1="8" y1="5" x2="108" y2="5" stroke="#999" stroke-width=".5"/>
      <g fill="#333"><circle cx="8" cy="5" r="3.5"/><circle cx="28" cy="5" r="3.5"/><circle cx="48" cy="5" r="3.5"/><circle cx="68" cy="5" r="3.5"/><circle cx="88" cy="5" r="3.5"/><circle cx="108" cy="5" r="3.5"/></g>
      <g stroke="#fff" stroke-width=".8" fill="none"><path d="M6.5 5l1 1 2-2M26.5 5l1 1 2-2M46.5 5l1 1 2-2M66.5 5l1 1 2-2M86.5 5l1 1 2-2M106.5 5l1 1 2-2"/></g>
      <rect x="0" y="12" width="16" height="8" fill="var(--orange-deep)"/><rect x="20" y="12" width="16" height="8" fill="var(--brown)"/><rect x="40" y="12" width="16" height="8" fill="var(--brown)"/><rect x="60" y="12" width="16" height="8" fill="var(--brown)"/><rect x="80" y="12" width="16" height="8" fill="var(--charcoal)"/><rect x="100" y="12" width="15" height="8" fill="var(--charcoal)"/>
    </svg>
  </div><span class="num">21</span><span class="star">★</span>
</div>

<!-- Row 4 -->
<div class="thumb" style="left:20px;top:378px">
  <div class="slide">
    <div class="photo" role="img" aria-label="Orange abstract light photograph" style="inset:0;background:linear-gradient(120deg,#f39a2d,#b55d1c 50%,#e8dccd)"></div>
    <div class="band" style="top:30px;height:16px;background:rgba(60,60,60,.75)"><b>Industries</b><span class="logo white" style="position:static;font-size:4.6px"><i></i>NEXORA</span></div>
  </div><span class="num">22</span>
</div>

<div class="thumb" style="left:187px;top:378px">
  <div class="slide">
    <div class="t">Transportation</div>
    <div class="photo" role="img" aria-label="City traffic at night with light trails" style="right:0;top:0;width:52px;height:72px;background:linear-gradient(160deg,#3e3a37,#d9822b 60%,#f1b057)"></div>
    <div class="p" style="left:5px;top:13px;width:64px"><b style="color:var(--orange)">Overview</b><br>Our transport systems link vehicles, depots and control rooms. We deliver fleet tracking, fare collection, passenger information and traffic data, with secure networks and support that keep services moving on time every day.</div>
  </div><span class="num">23</span><span class="star">★</span>
</div>

<div class="thumb" style="left:354px;top:378px">
  <div class="slide">
    <div class="t">System Components</div>
    <div class="p" style="left:5px;top:11px;width:115px">The system is made up of the following core parts:</div>
    <svg style="position:absolute;left:6px;top:20px" width="114" height="26" viewBox="0 0 114 26" aria-hidden="true">
      <circle cx="12" cy="13" r="11" fill="var(--orange-deep)"/><circle cx="35" cy="13" r="11" fill="#b24d1d"/><circle cx="58" cy="13" r="11" fill="#9a4420"/><circle cx="81" cy="13" r="11" fill="var(--brown)"/><circle cx="103" cy="13" r="11" fill="#5e2d18"/>
    </svg>
    <div class="p" style="left:5px;top:52px;width:115px">These parts work together to give full control and clear reports across the network.</div>
  </div><span class="num">24</span><span class="star">★</span>
</div>

<div class="thumb" style="left:521px;top:378px">
  <div class="slide">
    <div class="photo" role="img" aria-label="Office desk with plant photograph" style="inset:0;background:linear-gradient(120deg,#f2a341,#c46a22 45%,#dcd7cf)"></div>
    <div class="band" style="top:30px;height:16px;background:rgba(60,60,60,.75)"><b>Partnership</b><span class="logo white" style="position:static;font-size:4.6px"><i></i>NEXORA</span></div>
  </div><span class="num">25</span>
</div>

<div class="thumb" style="left:688px;top:378px">
  <div class="slide">
    <div class="t">Partnership</div>
    <svg style="position:absolute;left:18px;top:13px" width="90" height="56" viewBox="0 0 90 56" aria-hidden="true">
      <g fill="#c9c9c9"><rect x="0" y="0" width="18" height="7"/><rect x="22" y="0" width="22" height="7"/><rect x="48" y="0" width="16" height="7"/><rect x="68" y="0" width="20" height="7"/>
      <rect x="4" y="12" width="18" height="7"/><rect x="26" y="12" width="14" height="7"/><rect x="44" y="12" width="16" height="7"/><circle cx="70" cy="15.5" r="4"/>
      <rect x="0" y="24" width="16" height="7"/><rect x="20" y="24" width="20" height="7"/><rect x="44" y="24" width="22" height="7"/><rect x="70" y="24" width="16" height="7"/>
      <rect x="6" y="36" width="22" height="7"/><rect x="32" y="36" width="18" height="7"/><rect x="54" y="36" width="24" height="7"/>
      <rect x="16" y="48" width="20" height="6"/><rect x="42" y="48" width="24" height="6"/></g>
    </svg>
  </div><span class="num">26</span>
</div>

<div class="thumb" style="left:855px;top:378px">
  <div class="slide">
    <div class="photo" role="img" aria-label="Businessman touching digital interface" style="inset:0;background:linear-gradient(120deg,#1f2b3c,var(--photo-blue) 50%,#7d8ea6)"></div>
    <div class="band" style="top:26px;height:22px;background:rgba(60,60,60,.7)"><b>OUR COMPETENCIES<br>AND CAPACITY</b><span class="logo white" style="position:static;font-size:4px"><i></i>NEXORA</span></div>
  </div><span class="num">27</span>
</div>

<div class="thumb" style="left:1022px;top:378px">
  <div class="slide">
    <div class="t" style="font-size:4.6px">OUR COMPETENCIES AND CAPACITY</div><div class="logo" style="top:10px"><i></i>NEXORA</div>
    <div class="p" style="left:5px;top:13px;width:90px">Our company prides itself on skills in these areas:</div>
    <svg style="position:absolute;left:16px;top:20px" width="70" height="50" viewBox="0 0 70 50" aria-hidden="true">
      <g fill="var(--orange)"><circle cx="4" cy="4" r="3.5"/><circle cx="4" cy="15" r="3.5"/><circle cx="4" cy="26" r="3.5"/><circle cx="4" cy="37" r="3.5"/>
      <circle cx="52" cy="4" r="3.5"/><circle cx="52" cy="15" r="3.5"/><circle cx="52" cy="26" r="3.5"/></g>
    </svg>
    <div class="p" style="left:25px;top:21px;width:40px;line-height:11px">IT service management<br>Network infrastructure<br>Data centre services<br>Software development</div>
    <div class="p" style="left:73px;top:21px;width:48px;line-height:11px">ICT architecture<br>Voice and video<br>Managed print</div>
  </div><span class="num">28</span><span class="star">★</span>
</div>

<!-- Row 5 -->
<div class="thumb" style="left:20px;top:501px">
  <div class="slide">
    <div class="t" style="font-size:4.6px">OUR COMPETENCIES AND CAPACITY</div><div class="logo" style="top:10px"><i></i>NEXORA</div>
    <div class="p" style="left:5px;top:13px;width:100px">Our team holds broad skills across planning, delivery and support:</div>
    <svg style="position:absolute;left:44px;top:22px" width="38" height="38" viewBox="0 0 38 38" aria-hidden="true">
      <circle cx="19" cy="19" r="14" fill="none" stroke="var(--orange-deep)" stroke-width="5" stroke-dasharray="20 2"/>
      <circle cx="19" cy="19" r="8" fill="#fff"/>
      <rect x="14" y="16" width="10" height="7" rx="1" fill="var(--charcoal)"/><rect x="17" y="14" width="4" height="2.5" fill="none" stroke="var(--charcoal)" stroke-width=".8"/>
    </svg>
    <div class="p" style="left:18px;top:22px;width:24px;text-align:right">Project management</div>
    <div class="p" style="left:10px;top:38px;width:32px;text-align:right">Enterprise management and architecture</div>
    <div class="p" style="left:50px;top:62px;width:30px;text-align:center">Systems development</div>
    <div class="p" style="left:86px;top:24px;width:34px">Business analysis</div>
    <div class="p" style="left:86px;top:40px;width:34px">Network integration and support</div>
  </div><span class="num">29</span>
</div>

<div class="thumb" style="left:187px;top:501px">
  <div class="slide">
    <div class="photo" role="img" aria-label="Office desk with plant photograph" style="inset:0;background:linear-gradient(120deg,#f2a341,#c46a22 45%,#dcd7cf)"></div>
    <div class="band" style="top:28px;height:18px;background:rgba(60,60,60,.75)"><b>OUR Clients</b><span class="logo white" style="position:static;font-size:4.6px"><i></i>NEXORA</span></div>
  </div><span class="num">30</span>
</div>

<div class="thumb" style="left:354px;top:501px">
  <div class="slide">
    <div class="t">OUR Clients</div>
    <ul class="p" style="left:8px;top:13px;width:100px;line-height:3.4px"><li>Northline Projects</li><li>Harbor Transit Board</li><li>Alder Group</li><li>Verity Labs</li><li>Kestrel Engineering</li><li>Summit Motor Services</li><li>Brightwater Co</li><li>Ridge Supply</li><li>Caldera Estates</li><li>Orion Civil Works</li></ul>
  </div><span class="num">31</span>
</div>

<div class="thumb" style="left:521px;top:501px">
  <div class="slide">
    <div class="photo" role="img" aria-label="Office desk with plant photograph" style="inset:0;background:linear-gradient(120deg,#f2a341,#c46a22 45%,#dcd7cf)"></div>
    <div class="band" style="top:28px;height:18px;background:rgba(60,60,60,.75)"><b>OUR OFFICES</b><span class="logo white" style="position:static;font-size:4.6px"><i></i>NEXORA</span></div>
  </div><span class="num">32</span>
</div>

<div class="thumb" style="left:688px;top:501px">
  <div class="slide">
    <div class="t" style="font-size:4px">OUR OFFICES</div>
    <div class="p" style="left:6px;top:12px;width:110px"><b>LOCATIONS</b></div>
    <div class="p" style="left:6px;top:18px;width:110px;line-height:3.4px"><b style="color:var(--orange)">Head Office</b> – 1 Sample Road, Eastfield, 0000<br><b style="color:var(--orange)">Branch</b> – 22 Example Street, Westvale, 0001</div>
    <div class="p" style="left:6px;top:40px;width:110px;line-height:3.4px"><b style="color:var(--orange)">Contact</b> – Suite 4, Demo Park, Northgate<br>Tel: 000 000 0000<br>Fax: 000 000 0001<br>Email: info@nexora.example</div>
  </div><span class="num">33</span>
</div>

<div class="thumb" style="left:855px;top:501px">
  <div class="slide">
    <div class="photo" role="img" aria-label="Office desk photograph" style="left:0;top:0;right:0;height:32px;background:linear-gradient(90deg,#e9e6e1,#cfcac2)"></div>
    <div class="band" style="top:32px;height:22px;background:var(--orange)"><b style="font-size:7.5px;line-height:7px">TITLE PAGE<br><span style="font-size:3px;font-weight:400">Your subtitle here</span></b><span class="logo white" style="position:static;font-size:4px"><i></i>NEXORA</span></div>
  </div><span class="num">34</span>
</div>

<div class="drop-marker"></div>
</body>
</html>
```